Redesign existing website to have updated look and content

have existing website but do not have the time to put page detail that I want into it. we are a residential, family owned and operated HVAC and plumbing company. we offer service, repair, replacement, maintenance, new installations. the owner has over 20 years experience. got into his own business bc of high pricing charged by old employer. we believe CUSTOMER SERVICE IS THE ONLY THING THAT MATTERS, we are an harlow's guide top trade award winner. we just recently were invited to sell on Brindlemart. we currently have the owner and 1 other tech and a helper in the field. we want to keep small so that service doesn't suffer

Target Market(s)

homeowners over 28 in the Bucks and Montgomery and Delawre Counties of PA

Industry/Entity Type

Hvac

Number of Pages Required

4 page

Font styles to use
Serif
Sans Serif
Decorative

Colors
0255a3
ec1f27

Requirements
Must have
• more content and information
• online scheduling thru V Cita
• information that is not related to HVAC that can be updated daily
Nice to have
• apps that customers will be drawn to website with
• information regarding our services and costs
• online scheduling
• better content!!!!
• links to vendors and outside information

```html
<!DOCTYPE html>
<html lang="en">
<head>
<meta charset="utf-8">
<title>Kestrel Service – Heating, Air Conditioning &amp; Plumbing</title>
<link rel="stylesheet" href="https://fonts.googleapis.com/css2?family=Open+Sans:wght@400;600;700&display=swap">
<style>
:root{
  --blue:#0255a3;
  --blue-dark:#023f7a;
  --red:#ec1f27;
  --ink:#333;
  --muted:#777;
  --light:#f4f4f4;
  --navy:#0e1c33;
  --navy-deep:#081224;
  --white:#fff;
}
*{box-sizing:border-box;margin:0;padding:0}
html,body{width:755px;height:1200px;overflow:hidden}
body{font-family:"Open Sans",Arial,sans-serif;color:var(--ink);background:var(--white);font-size:8px;line-height:1.45}
a{color:inherit;text-decoration:none}

/* header */
.site-header{height:75px;display:flex;align-items:center;justify-content:space-between;padding:0 42px}
.brand{display:flex;align-items:center;gap:8px}
.brand-dot{width:26px;height:26px;border-radius:50%;background:var(--red)}
.brand-name{font-weight:700;font-size:21px;color:var(--blue);line-height:1}
.top-contact{display:flex;gap:16px;font-size:9px;color:var(--ink);align-self:flex-start;margin-top:28px}
.top-contact span{display:flex;align-items:center;gap:5px}

/* nav */
.main-nav{height:30px;background:var(--blue);display:flex;align-items:center;padding:0 42px}
.main-nav a{color:var(--white);font-size:9px;padding:0 16px;height:30px;line-height:30px}
.main-nav a.active{background:var(--red)}
.search-btn{margin-left:auto;width:20px;height:20px;border-radius:50%;background:var(--red);display:flex;align-items:center;justify-content:center}

/* hero */
.hero{position:relative;height:230px;background:linear-gradient(160deg,#c9d3dc 0%,#8ea5ba 45%,#3e5f86 75%,#c7ccd2 100%)}
.hero-caption{position:absolute;left:0;right:0;top:150px;text-align:center;color:var(--white);font-size:14px;background:rgba(0,0,0,.25);padding:6px 0}
.dots{position:absolute;bottom:14px;left:0;right:0;display:flex;justify-content:center;gap:4px}
.dots i{width:5px;height:5px;border-radius:50%;background:rgba(255,255,255,.6)}
.dots i.on{background:var(--white)}

/* services */
.services{display:flex;justify-content:space-between;padding:12px 62px 0;height:225px}
.service-card{width:115px;text-align:center;padding:10px 8px 0}
.service-card.featured{background:var(--blue);color:var(--white);height:200px}
.service-card h3{font-weight:400;font-size:13px;margin-bottom:10px}
.service-icon{width:50px;height:50px;border-radius:50%;background:var(--blue);margin:0 auto 10px;display:flex;align-items:center;justify-content:center}
.featured .service-icon{background:var(--white)}
.service-card p{font-size:6.5px;color:var(--muted);margin-bottom:8px}
.featured p{color:#dce8f5}
.btn{display:inline-flex;align-items:center;gap:4px;background:var(--red);color:var(--white);font-size:7px;padding:4px 9px}

/* scheduling */
.scheduling{height:158px;background:linear-gradient(180deg,#3b4048,#23272d);color:var(--white);text-align:center;padding-top:18px}
.section-title{font-weight:400;font-size:16px;margin-bottom:8px}
.scheduling p{width:620px;margin:0 auto 8px;font-size:6.5px;color:#cfd3d8}
.schedule-link{display:block;color:#8fb8e6;font-size:7px;margin-bottom:10px}
.btn-blue{background:var(--blue)}

/* news */
.news{height:155px;text-align:center;padding-top:14px;background:var(--light)}
.news .section-title{color:var(--red);font-size:17px}
.news-list{display:flex;justify-content:center;gap:28px;margin-top:6px;text-align:left}
.news-item{display:flex;gap:8px;width:190px}
.news-date{flex:none;width:36px;height:36px;border-radius:50%;background:var(--red);color:var(--white);text-align:center;font-size:12px;font-weight:700;line-height:1;padding-top:7px}
.news-date small{display:block;font-size:6px;font-weight:400}
.news-item h4{font-size:7.5px;color:var(--red);font-weight:600;margin-bottom:3px}
.news-item p{font-size:6.5px;color:var(--muted)}
.news .dots{position:static;margin-top:18px}
.news .dots i{background:#c8c8c8}
.news .dots i.on{background:var(--red)}

/* welcome */
.welcome{height:160px;background:linear-gradient(180deg,#4a4e55,#2b2f35);color:var(--white);text-align:center;padding-top:26px}
.welcome .section-title{font-size:18px}
.welcome p{width:640px;margin:0 auto 12px;font-size:6.5px;color:#d5d8dc}

/* footer */
.site-footer{height:155px;background:var(--navy);color:#c9d2df;display:flex;gap:26px;padding:14px 42px 0}
.site-footer h5{color:var(--white);font-weight:400;font-size:10px;margin-bottom:7px}
.footer-nav{width:85px}
.footer-nav li{list-style:none;font-size:6.5px;line-height:12px}
.footer-nav li::before{content:"› ";color:var(--red)}
.testimonial{width:165px}
.testimonial-body{display:flex;gap:6px}
.avatar{flex:none;width:32px;height:32px;border-radius:50%;background:linear-gradient(135deg,#b89a7e,#6c5648)}
.testimonial strong{color:var(--white);font-size:7px;display:block}
.testimonial p{font-size:6.5px}
.testimonial .more{color:var(--red);font-size:6.5px;margin-top:4px;display:block}
.share{width:190px}
.share p{font-size:6.5px;margin-bottom:6px}
.share-form{display:flex;margin-bottom:8px}
.share-form span{flex:1;background:var(--white);color:#999;font-size:6.5px;padding:4px 6px}
.share-form b{background:var(--red);color:var(--white);font-weight:400;font-size:6.5px;padding:4px 10px}
.social{display:flex;gap:5px}
.social i{width:15px;height:15px;border-radius:50%;background:var(--red)}
.social i:nth-child(2){background:var(--blue)}
.social i:nth-child(4){background:#e58a1f}
.contact{width:140px;font-size:6.5px}
.contact dl{display:grid;grid-template-columns:30px 1fr;row-gap:3px;margin-bottom:8px}
.contact dt{color:var(--white)}
.partner{display:flex;align-items:center;gap:8px}
.partner-badge{width:22px;height:22px;background:#d8d8d8}
.partner-name{background:var(--white);color:var(--ink);font-weight:700;font-size:11px;padding:3px 7px}
.copyright{height:15px;background:var(--navy-deep);color:#8a97aa;font-size:6px;text-align:center;line-height:15px}
</style>
</head>
<body>

<header class="site-header">
  <a class="brand" href="#"><span class="brand-dot"></span><span class="brand-name">Kestrel Service</span></a>
  <div class="top-contact">
    <span><svg width="9" height="9" viewBox="0 0 24 24"><path fill="#ec1f27" d="M6.6 10.8a15 15 0 006.6 6.6l2.2-2.2c.3-.3.7-.4 1-.2 1.1.4 2.3.6 3.6.6.6 0 1 .4 1 1V20c0 .6-.4 1-1 1C10.6 21 3 13.4 3 4c0-.6.4-1 1-1h3.5c.6 0 1 .4 1 1 0 1.3.2 2.5.6 3.6.1.3 0 .7-.2 1z"/></svg>0700 555 0182</span>
    <span><svg width="10" height="8" viewBox="0 0 24 18"><rect x="1" y="1" width="22" height="16" fill="none" stroke="#ec1f27" stroke-width="2"/><path d="M1 1l11 9 11-9" fill="none" stroke="#ec1f27" stroke-width="2"/></svg>service@kestrelhvac.example</span>
  </div>
</header>

<nav class="main-nav">
  <a class="active" href="#">Home</a><a href="#">About</a><a href="#">Service</a><a href="#">News</a><a href="#">Blogs</a><a href="#">Contact</a>
  <span class="search-btn"><svg width="9" height="9" viewBox="0 0 24 24"><circle cx="10" cy="10" r="7" fill="none" stroke="#fff" stroke-width="3"/><path d="M15 15l7 7" stroke="#fff" stroke-width="3"/></svg></span>
</nav>

<section class="hero" role="img" aria-label="Technician working on ceiling air-conditioning ductwork">
  <p class="hero-caption">Aenean pharetra. Ex putant intellegat deseruisse ius, no</p>
  <div class="dots"><i></i><i class="on"></i><i></i><i></i></div>
</section>

<section class="services">
  <article class="service-card featured">
    <h3>Service</h3>
    <div class="service-icon"><svg width="24" height="24" viewBox="0 0 24 24"><circle cx="12" cy="12" r="6" fill="none" stroke="#0255a3" stroke-width="3"/><circle cx="12" cy="12" r="2" fill="#0255a3"/></svg></div>
    <p>Family technicians on call for fast, honest work with clear prices quoted before any job begins.</p>
    <a class="btn" href="#">Read More ›</a>
  </article>
  <article class="service-card">
    <h3>Repair</h3>
    <div class="service-icon"><svg width="24" height="24" viewBox="0 0 24 24"><path d="M4 20l9-9M14 4a5 5 0 006 6l-3 3-6-6z" fill="none" stroke="#fff" stroke-width="2.5"/></svg></div>
    <p>Family technicians on call for fast, honest work with clear prices quoted before any job begins.</p>
    <a class="btn" href="#">Read More ›</a>
  </article>
  <article class="service-card">
    <h3>Replacement</h3>
    <div class="service-icon"><svg width="24" height="24" viewBox="0 0 24 24"><path d="M5 12a7 7 0 0112-5l2-2v6h-6l2-2a4 4 0 00-7 3zM19 12a7 7 0 01-12 5l-2 2v-6h6l-2 2a4 4 0 007-3z" fill="#fff"/></svg></div>
    <p>Family technicians on call for fast, honest work with clear prices quoted before any job begins.</p>
    <a class="btn" href="#">Read More ›</a>
  </article>
  <article class="service-card">
    <h3>Maintenance</h3>
    <div class="service-icon"><svg width="24" height="24" viewBox="0 0 24 24"><path d="M12 3v4M12 17v4M3 12h4M17 12h4" stroke="#fff" stroke-width="2.5"/><circle cx="12" cy="12" r="4" fill="none" stroke="#fff" stroke-width="2.5"/></svg></div>
    <p>Family technicians on call for fast, honest work with clear prices quoted before any job begins.</p>
    <a class="btn" href="#">Read More ›</a>
  </article>
  <article class="service-card">
    <h3>New Installations</h3>
    <div class="service-icon"><svg width="24" height="24" viewBox="0 0 24 24"><path d="M12 5v14M5 12h14" stroke="#fff" stroke-width="3"/></svg></div>
    <p>Family technicians on call for fast, honest work with clear prices quoted before any job begins.</p>
    <a class="btn" href="#">Read More ›</a>
  </article>
</section>

<section class="scheduling" role="img" aria-label="Darkened photo of technician tools behind scheduling section">
  <h2 class="section-title">Online Scheduling</h2>
  <p>Book your visit online in a few clicks. Pick a time that suits you and our small team will arrive ready to help with heating, cooling or plumbing. We keep our crew small so every customer gets the care they deserve.</p>
  <a class="schedule-link" href="#">www.bookslot.example/kestrel</a>
  <a class="btn btn-blue" href="#">Book Now ›</a>
</section>

<section class="news">
  <h2 class="section-title">Today News</h2>
  <div class="news-list">
    <article class="news-item"><div class="news-date">06<small>Aug</small></div><div><h4>DESIGN COLOR</h4><p>Simple tips to keep your home comfortable this season, from filter changes to checking your thermostat settings.</p></div></article>
    <article class="news-item"><div class="news-date">06<small>Aug</small></div><div><h4>DESIGN COLOR</h4><p>Simple tips to keep your home comfortable this season, from filter changes to checking your thermostat settings.</p></div></article>
    <article class="news-item"><div class="news-date">06<small>Aug</small></div><div><h4>DESIGN COLOR</h4><p>Simple tips to keep your home comfortable this season, from filter changes to checking your thermostat settings.</p></div></article>
  </div>
  <div class="dots"><i></i><i class="on"></i><i></i></div>
</section>

<section class="welcome" role="img" aria-label="Darkened photo of a heating and air conditioning unit">
  <h2 class="section-title">Welcome to Kestrel Service Heating &amp; Air Conditioning</h2>
  <p>Over twenty years in the trade taught our owner one thing: customer service is the only thing that matters. We are a family owned and operated company serving homeowners in Bucks, Montgomery and Delaware Counties with fair, upfront pricing.</p>
  <a class="btn" href="#">Learn More ›</a>
</section>

<footer class="site-footer">
  <div class="footer-nav">
    <h5>Navigation</h5>
    <ul><li>HOME</li><li>ABOUT</li><li>SERVICE</li><li>NEWS</li><li>BLOG</li><li>CONTACT</li></ul>
  </div>
  <div class="testimonial">
    <h5>Testimonial</h5>
    <div class="testimonial-body">
      <div class="avatar" role="img" aria-label="Customer portrait"></div>
      <div><strong>Dana M.</strong><p>Friendly, on time and honest. They fixed our furnace the same day and explained every step. We will call them again.</p><a class="more" href="#">Read More</a></div>
    </div>
  </div>
  <div class="share">
    <h5>Share your thought</h5>
    <p>Tell us how we did or ask a question. We read every message and reply within one business day.</p>
    <div class="share-form"><span>Your email</span><b>Send</b></div>
    <div class="social"><i></i><i></i><i></i><i></i><i></i></div>
  </div>
  <div class="contact">
    <h5>CONTACT US</h5>
    <dl><dt>Phone</dt><dd>0700 555 0182</dd><dt>Fax</dt><dd>0700 555 0183</dd><dt>Email</dt><dd>service@kestrelhvac.example</dd></dl>
    <div class="partner"><span class="partner-badge"></span><span class="partner-name">Brindlemart</span></div>
  </div>
</footer>
<div class="copyright">Copyright 2015. All Rights Reserved</div>

</body>
</html>
```